2 x storefront vinyl request

We are transitioning to a storefront office and need two vinyls for the windows.

First vinyl: Use the Dalton Rivers logo, website (www.daltonriversholdings.example) and leasing office number ((555) 318-4472)

Second vinyl: Maintenance Division & phone number (555) 318-4472

```html
<!DOCTYPE html>
<html lang="en">
<head>
<meta charset="utf-8">
<title>Dalton Rivers Properties – Storefront Vinyls</title>
<link href="https://fonts.googleapis.com/css2?family=Arimo:wght@400;700&display=swap" rel="stylesheet">
<style>
  :root {
    --glass: #a4a4a6;
    --vinyl: #ffffff;
    --ink-grey: #8a8a8c;
  }
  html, body {
    margin: 0;
    padding: 0;
    width: 1200px;
    height: 1200px;
    overflow: hidden;
  }
  body {
    background: var(--glass);
    font-family: "Arimo", Arial, sans-serif;
    color: var(--vinyl);
    position: relative;
  }
  .vinyl {
    position: absolute;
    top: 50%;
    transform: translateY(-50%);
  }

  /* Maintenance vinyl */
  .maintenance {
    left: 40px;
    width: 520px;
    display: flex;
    flex-direction: column;
    align-items: center;
  }
  .maintenance .arc-title {
    width: 520px;
    height: 190px;
    display: block;
  }
  .maintenance .arc-title text {
    fill: var(--vinyl);
    font-family: "Arimo", Arial, sans-serif;
    font-weight: 700;
    font-size: 40px;
    letter-spacing: 3px;
  }
  .brand {
    display: flex;
    align-items: center;
    gap: 18px;
  }
  .brand-mark {
    width: 30px;
    height: 30px;
    border: 5px solid var(--vinyl);
    box-sizing: border-box;
  }
  .brand-name {
    font-weight: 700;
    font-size: 30px;
    line-height: 1.08;
    text-transform: uppercase;
    color: var(--vinyl);
  }
  .maintenance .brand {
    margin-top: -50px;
  }
  .phone-plate {
    margin-top: 70px;
    width: 520px;
    height: 82px;
    background: var(--vinyl);
    color: var(--ink-grey);
    font-weight: 700;
    font-size: 48px;
    display: flex;
    align-items: center;
    justify-content: center;
  }

  /* Leasing vinyl */
  .leasing {
    right: 40px;
    width: 520px;
    border: 12px solid var(--vinyl);
    box-sizing: border-box;
    display: flex;
    flex-direction: column;
    align-items: center;
  }
  .leasing .brand {
    margin-top: 90px;
  }
  .website {
    margin-top: 90px;
    margin-bottom: 22px;
    font-weight: 700;
    font-size: 20px;
    color: var(--vinyl);
  }
  .leasing .phone-band {
    width: 100%;
    height: 96px;
    background: var(--vinyl);
    color: var(--ink-grey);
    font-weight: 700;
    font-size: 48px;
    display: flex;
    align-items: center;
    justify-content: center;
  }
</style>
</head>
<body>

  <section class="vinyl maintenance">
    <svg class="arc-title" viewBox="0 0 520 190" aria-label="Maintenance Division">
      <defs>
        <path id="title-arc" d="M 20 185 A 250 210 0 0 1 500 185"/>
      </defs>
      <text text-anchor="middle">
        <textPath href="#title-arc" startOffset="50%">MAINTENANCE DIVISION</textPath>
      </text>
    </svg>
    <div class="brand">
      <span class="brand-mark"></span>
      <span class="brand-name">Dalton Rivers<br>Properties</span>
    </div>
    <div class="phone-plate">(555) 318-4472</div>
  </section>

  <section class="vinyl leasing">
    <div class="brand">
      <span class="brand-mark"></span>
      <span class="brand-name">Dalton Rivers<br>Properties</span>
    </div>
    <div class="website">www.daltonriversholdings.example</div>
    <div class="phone-band">(555) 318-4472</div>
  </section>

</body>
</html>
```